Robotic Physical Therapy office needs a Grand Opening Flyer

We need a Grand Opening flyer design for a robotic physical therapy office named Stellar Motion Therapy. We would like it to have a clean, classy, upscale feeling that gives potential clients a V.I.P. feeling. We would like to use the colors black, gray, and yellow (logo will be uploaded).

Event: Thursday, June 1st, 2023 from 12pm-6pm
location: 58274 Harlow Ave, Bloomfield Hills, MI 48319

Industry/Entity Type

Physical therapy

Font styles to use
Script

Colors

Designer to choose colors to be used in the design.

Requirements
Nice to have
• More of a vip feel for the invite

```html
<!DOCTYPE html>
<html lang="en">
<head>
<meta charset="utf-8">
<title>Stellar Motion Therapy – Grand Opening</title>
<link rel="stylesheet" href="https://fonts.googleapis.com/css2?family=Kumbh+Sans:wght@400;700&display=swap">
<style>
  :root {
    --backdrop: #c9c9cb;
    --paper: #ffffff;
    --ink: #2b2a35;
    --text: #1f1f1f;
    --yellow: #e8d431;
    --yellow-deep: #a99a12;
    --shade: #2f3020;
    --deco-gray: #f1f1f2;
    --deco-yellow: #fbf7dc;
  }
  html, body {
    margin: 0;
    width: 1200px;
    height: 1200px;
    overflow: hidden;
    background: var(--backdrop);
    font-family: "Kumbh Sans", sans-serif;
  }
  .flyer {
    position: absolute;
    left: 225px;
    top: 69px;
    width: 906px;
    height: 1062px;
    background: var(--paper);
    box-shadow: 0 2px 6px rgba(0,0,0,.18);
    overflow: hidden;
  }
  .flyer__art {
    position: absolute;
    inset: 0;
    width: 906px;
    height: 1062px;
  }
  .brand {
    position: absolute;
    top: 52px;
    left: 0;
    width: 906px;
    display: flex;
    justify-content: center;
    align-items: center;
    gap: 18px;
    padding-right: 150px;
    box-sizing: border-box;
  }
  .brand__dot {
    width: 70px;
    height: 70px;
    border-radius: 50%;
    background: var(--yellow);
    flex: none;
  }
  .brand__name {
    margin: 0;
    color: var(--ink);
    font-weight: 700;
    font-size: 40px;
    line-height: 1.02;
    text-transform: uppercase;
    letter-spacing: .5px;
  }
  .details {
    position: absolute;
    left: 0;
    top: 810px;
    width: 752px;
    text-align: center;
    color: var(--text);
  }
  .details p { margin: 0; }
  .details__label { font-weight: 700; }
  .details__event { font-size: 25px; line-height: 33px; }
  .details__location { margin-top: 24px !important; font-size: 23px; line-height: 32px; }
  .details__location .details__label { font-size: 29px; display: block; }
</style>
</head>
<body>
  <main class="flyer">
    <svg class="flyer__art" viewBox="180 55 725 850" xmlns="http://www.w3.org/2000/svg">
      <defs>
        <linearGradient id="photoTone" x1="0" y1="0" x2="1" y2="1">
          <stop offset="0" stop-color="#e6d23a"/>
          <stop offset=".45" stop-color="#c6b322"/>
          <stop offset=".75" stop-color="#6f6a1e"/>
          <stop offset="1" stop-color="#2f3020"/>
        </linearGradient>
      </defs>
      <g class="deco deco--gray" stroke="var(--deco-gray)" stroke-width="30" stroke-linecap="round" fill="none">
        <line x1="740" y1="630" x2="930" y2="440"/>
        <line x1="660" y1="760" x2="930" y2="500"/>
        <line x1="720" y1="830" x2="930" y2="620"/>
        <line x1="800" y1="880" x2="930" y2="750"/>
      </g>
      <g class="deco deco--yellow" stroke="var(--deco-yellow)" stroke-width="28" stroke-linecap="round" fill="none">
        <line x1="180" y1="770" x2="200" y2="750"/>
        <line x1="180" y1="830" x2="250" y2="760"/>
        <line x1="200" y1="880" x2="300" y2="790"/>
        <line x1="280" y1="890" x2="350" y2="830"/>
      </g>
      <g class="gallery" role="img" aria-label="Photo of a patient walking on a treadmill in a robotic leg exoskeleton beside a monitor, tinted yellow, seen through rounded window cut-outs" fill="url(#photoTone)">
        <rect x="237" y="230" width="79" height="337" rx="39.5"/>
        <circle cx="382.5" cy="302" r="39.5"/>
        <rect x="343" y="373" width="79" height="274" rx="39.5"/>
        <rect x="448" y="230" width="79" height="255" rx="39.5"/>
        <circle cx="487.5" cy="561" r="39.5"/>
        <circle cx="593.5" cy="303" r="39.5"/>
        <rect x="554" y="373" width="79" height="274" rx="39.5"/>
        <rect x="660" y="230" width="79" height="337" rx="39.5"/>
      </g>
    </svg>

    <header class="brand">
      <span class="brand__dot" aria-hidden="true"></span>
      <h1 class="brand__name">Stellar Motion<br>Therapy</h1>
    </header>

    <section class="details">
      <p class="details__event"><span class="details__label">Event:</span> Thursday, June 1st, 2023<br>from 12pm-6pm</p>
      <p class="details__location"><span class="details__label">Location:</span>58274 Harlow Ave, Bloomfield Hills, MI 48319</p>
    </section>
  </main>
</body>
</html>
```